WORD Template for Training Manual called Lantern Road

I have written a training manual called Lantern Road. I need a design for the manual I can put the materials into for small groups of people to use.
This means a cover along with a page design that looks appealing but doesn't distract from the content.
We already have an organisational logo and colour scheme. It would be great to have at nine different page designs as the manual will have nine sessions of learning. So one design for each session of content.
I have uploaded some of the example materials we have designed from another designer as well so you can see the kind of look and feel our other materials have.
I have also uploaded the introduction and the first session of the content so you can use it to help shape the design.
As you will see in the sessions, each session has small group activities, discussion questions and a video content session for the group to watch. All nine sessions will be designed in a similar way.
There will also be a second booklet to design of daily reflections so a successful design for this workbook will lead to a second project with the same look and feel.
Updates
Need extra days to review
Target Market(s)
My target market is adults from 18-45
Industry/Entity Type
Christian Ministry
Look and feel
Each slider illustrates characteristics of the customer's brand and the style your logo design should communicate.

```html
<!DOCTYPE html>
<html lang="en">
<head>
<meta charset="utf-8">
<title>Lantern Road – Training Manual Layout</title>
<link href="https://fonts.googleapis.com/css2?family=Montserrat:wght@500;700;800;900&family=Open+Sans:wght@400;600;700&display=swap" rel="stylesheet">
<style>
  :root{
    --ink:#2b2b2b;
    --muted:#5a5a5a;
    --black:#0d0d0d;
    --red:#e5262b;
    --green:#7cc142;
    --pink:#f3a3bd;
    --pink-deep:#e86f9a;
    --purple:#6e3fa3;
    --purple-deep:#5a2f8c;
    --lilac:#b18ad8;
    --yellow:#ffe14f;
    --grey-box:#e6e6e8;
    --paper:#ffffff;
    --stage:#f4f4f5;
  }
  *{box-sizing:border-box;margin:0;padding:0}
  html,body{width:1200px;height:2400px;overflow:hidden}
  body{background:var(--stage);font-family:"Open Sans",Arial,sans-serif;color:var(--ink);position:relative}
  .sheet{position:absolute;box-shadow:0 6px 22px rgba(0,0,0,.16);overflow:hidden}

  /* Cover */
  .cover{left:370px;top:20px;width:460px;height:680px;background:var(--black);color:#fff;text-align:center}
  .cover-head{position:relative;z-index:2}
  .cover-title{font-family:"Montserrat",Arial,sans-serif;font-weight:900;font-size:64px;line-height:.95;letter-spacing:1px;padding-top:50px}
  .cover-title .word-one{color:var(--red);display:block}
  .cover-title .word-two{color:var(--green);display:block}
  .cover-sub{font-family:"Montserrat",Arial,sans-serif;font-weight:700;font-size:13px;line-height:1.45;letter-spacing:.5px;margin:18px auto 0;width:340px}
  .cover-photo{position:absolute;left:0;top:285px;width:460px;height:345px;z-index:1;
    background:radial-gradient(circle at 52% 50%,#9fdc55 0%,#4f8f2a 14%,#1f3316 34%,#2a2a2a 55%,#0d0d0d 80%)}
  .cover-brand{position:absolute;right:22px;bottom:18px;z-index:2;display:flex;align-items:center;gap:8px;font-family:"Montserrat",Arial,sans-serif;font-weight:700;font-size:14px;color:#fff}
  .cover-brand .dot{width:14px;height:14px;border-radius:50%;background:var(--green)}

  /* Spreads */
  .spread{left:150px;width:900px;display:flex;background:var(--paper)}
  .page{width:450px;height:100%;position:relative}
  .intro-spread{top:740px;height:520px}
  .intro-page{background:var(--pink);padding:34px 30px}
  .intro-page h2{font-family:"Montserrat",Arial,sans-serif;font-size:15px;font-weight:800;color:var(--ink);margin-bottom:10px;letter-spacing:.5px}
  .intro-cols{column-count:2;column-gap:22px;font-size:8.6px;line-height:1.55;color:var(--ink)}
  .intro-cols p{margin-bottom:7px}
  .week-page{background:var(--purple);display:flex;flex-direction:column;align-items:center;justify-content:center}
  .week-page .edge{position:absolute;left:0;top:0;width:26px;height:100%;background:var(--pink)}
  .week-label{font-family:"Montserrat",Arial,sans-serif;font-weight:800;color:var(--yellow);font-size:22px;letter-spacing:2px;margin-top:12px}
  .week-rule{width:150px;height:2px;background:#fff;margin:16px 0}
  .week-title{font-family:"Montserrat",Arial,sans-serif;font-weight:800;color:#fff;font-size:24px;letter-spacing:1px}

  .session-spread{top:1320px;height:1040px}
  .session-page{padding:44px 26px 44px 44px;display:flex;gap:22px;font-size:8.8px;line-height:1.55}
  .session-page.right{padding-left:30px}
  .band-top,.band-bottom{position:absolute;left:0;width:100%;height:16px}
  .band-top{top:0}.band-bottom{bottom:0}
  .left .band-top,.left .band-bottom{background:var(--purple)}
  .right .band-top,.right .band-bottom{background:var(--pink)}
  .side-bar{position:absolute;left:0;top:16px;width:14px;height:calc(100% - 32px);background:var(--lilac)}
  .col{flex:1;display:flex;flex-direction:column;gap:10px}
  .icon{width:34px;height:34px}
  .heading{font-family:"Montserrat",Arial,sans-serif;font-weight:800;font-size:12px;line-height:1.25;letter-spacing:.3px}
  .heading.purple{color:var(--purple)}
  .heading.pink{color:var(--pink-deep)}
  .mark{background:var(--yellow);padding:0 2px}
  ul.points{padding-left:12px}
  ul.points li{margin-bottom:4px}
  .grey-box{background:var(--grey-box);padding:12px}
  .callout{font-family:"Montserrat",Arial,sans-serif;font-weight:700;font-size:9.5px;color:var(--pink-deep)}
</style>
</head>
<body>

<section class="sheet cover">
  <div class="cover-head">
    <h1 class="cover-title"><span class="word-one">LANTERN</span><span class="word-two">ROAD</span></h1>
    <p class="cover-sub">60 DAYS OF LEARNING THAT WILL TEACH YOU TO LEAP FROM SAFETY INTO THE ADVENTURE OF YOUR LIFE!</p>
  </div>
  <div class="cover-photo" role="img" aria-label="Photograph of a green seedling sprouting from dark soil"></div>
  <div class="cover-brand"><span class="dot"></span>Hearth Fellowship</div>
</section>

<section class="sheet spread intro-spread">
  <div class="page intro-page">
    <h2>INTRODUCTION</h2>
    <div class="intro-cols">
      <p>When we set out to follow a calling, most of us expect a clear map. Instead we find a road that bends, climbs and sometimes disappears into fog. This manual was written for people who want to walk that road together, honestly and with courage.</p>
      <p>Over the coming weeks your group will explore what it means to trust, to risk and to love well. Each session gives space to listen, to talk and to try something new in everyday life.</p>
      <p>You do not need to have every answer. You only need to show up, bring your questions and be willing to share them with others who are walking the same way.</p>
      <p>Each week begins with a short topic overview and clear goals. A video is then shared with the whole group, followed by large group discussion and smaller circles where deeper conversation can happen.</p>
      <p>Leaders will find notes on timing and the resources needed for each session. Participants will find prompts to reflect on during the week and space to write down thoughts, prayers and next steps.</p>
      <p>Our hope is simple: that by the end of these sessions you will feel more at home in faith, more connected to the people around you and more ready to step out into the adventure ahead.</p>
      <p>Take your time. Read slowly. Let each question settle before you move on. Growth rarely comes in a rush, and the road is best walked at a steady pace.</p>
    </div>
  </div>
  <div class="page week-page">
    <div class="edge"></div>
    <svg width="70" height="70" viewBox="0 0 70 70" fill="none" stroke="#fff" stroke-width="3" stroke-linejoin="round" aria-hidden="true">
      <rect x="8" y="12" width="54" height="50" rx="4"/>
      <line x1="8" y1="26" x2="62" y2="26"/>
      <line x1="22" y1="5" x2="22" y2="18"/>
      <line x1="48" y1="5" x2="48" y2="18"/>
      <line x1="26" y1="44" x2="44" y2="44"/>
    </svg>
    <div class="week-label">WEEK ONE</div>
    <div class="week-rule"></div>
    <div class="week-title">WHAT IS LOVE?</div>
  </div>
</section>

<section class="sheet spread session-spread">
  <div class="page session-page left">
    <div class="band-top"></div><div class="side-bar"></div><div class="band-bottom"></div>
    <div class="col">
      <svg class="icon" viewBox="0 0 34 34" aria-hidden="true"><rect x="3" y="6" width="28" height="22" rx="3" fill="var(--purple)"/><path d="M10 28l-4 5v-5z" fill="var(--purple)"/></svg>
      <div class="heading purple">TOPIC:</div>
      <p><span class="mark">Love is a choice</span> demonstrated by action. In this week we look at how love moves from feeling to deciding, and why that matters for every relationship.</p>
      <div class="heading purple">IN THIS SESSION, PARTICIPANTS WILL LEARN TO:</div>
      <ul class="points">
        <li>Explain the difference between love as a feeling and love as a daily choice.</li>
        <li>Describe ways love shows up in small, ordinary moments.</li>
        <li>Name one person they will intentionally serve this week.</li>
      </ul>
      <svg class="icon" viewBox="0 0 34 34" aria-hidden="true"><rect x="4" y="4" width="26" height="26" rx="4" fill="var(--pink-deep)"/><line x1="10" y1="13" x2="24" y2="13" stroke="#fff" stroke-width="2.5"/><line x1="10" y1="20" x2="24" y2="20" stroke="#fff" stroke-width="2.5"/></svg>
      <div class="heading pink">RESOURCES YOU WILL NEED</div>
      <p>A copy of this manual for each person, pens, sticky notes, and a screen with speakers to play the session video.</p>
    </div>
    <div class="col">
      <svg class="icon" viewBox="0 0 34 34" aria-hidden="true"><rect x="3" y="7" width="28" height="20" rx="3" fill="var(--pink-deep)"/><path d="M14 12l8 5-8 5z" fill="#fff"/></svg>
      <div class="heading pink">PRE VIDEO ACTIVITY</div>
      <p>In groups of three, share a moment when someone showed you love in a way you did not expect. What did they do, and how did it change your day?</p>
      <p>Write one word on a sticky note that describes how that moment made you feel. Place the notes on a wall where everyone can see them before the video begins.</p>
      <p class="callout">SHOW VIDEO CONTENT FOR WEEK 1 (15 MINUTES)</p>
      <div class="heading purple">LARGE GROUP DISCUSSION</div>
      <ul class="points">
        <li>Which line in the video stayed with you the most, and why?</li>
        <li>Where have you seen love described only as a feeling?</li>
        <li>What would change if love were first a decision?</li>
      </ul>
    </div>
  </div>
  <div class="page session-page right">
    <div class="band-top"></div><div class="band-bottom"></div>
    <div class="col">
      <div class="heading purple">SMALL GROUP DISCUSSION</div>
      <p>In groups of four, discuss the following questions.</p>
      <ul class="points">
        <li>When a close friend is hurting, what do you usually do first? What does that reveal about how you love?</li>
        <li>Think of a time you chose to love someone when you did not feel like it. What helped you choose?</li>
        <li>Read the short passage on the next page aloud together. Which words challenge you most?</li>
      </ul>
      <div class="grey-box">
        <p>Leader note: allow each person time to speak. Silence is fine. Gently invite quieter members to share if they are comfortable, but never press.</p>
      </div>
      <ul class="points">
        <li>What might love look like in your home this week?</li>
        <li>How can this group encourage you to follow through?</li>
      </ul>
    </div>
    <div class="col">
      <p>If you are unsure where to start, choose one small, practical act: a meal, a message, an hour of listening. Love grows through repeated, simple choices.</p>
      <ul class="points">
        <li>Who is one person you find hard to love right now?</li>
        <li>What is one step you could take toward them?</li>
        <li>What might stop you, and how can you prepare for it?</li>
      </ul>
      <p>Close the small group time by praying for each other by name.</p>
      <div class="heading purple">LARGE GROUP DISCUSSION</div>
      <div class="grey-box">
        <p>Come back together as one group and invite each small group to share one insight they discovered.</p>
        <p><span class="mark">End the evening with a time of prayer.</span></p>
      </div>
    </div>
  </div>
</section>

</body>
</html>
```